Upmarket Bathroom and Kitchen ware supplier needs a classy business card design

We are a company based in Fiji, we sell plumbing ware (Kitchen and bathroom taps, Basins,showers, toilets etc) through up market show rooms to individuals and directly through Architects and designers of resorts and holiday houses for new builds and renovations. we are wanting to upgrade our over all look and brand. we are starting with a new logo but will be rebranding the whole business. This project is for a business card design for my management and tales team I would like it to be dark, classy and interesting

Target Market(s)

Resort directors and Management, High end holiday home owners

Contact Information for Business Card

Neil Dawson
Director
+64219473815

Colors

Designer to choose colors to be used in the design.

Requirements
Must have
• Must have an upmarket appearance I like darker charcoal shades but will be guided by the designers
• Please any catch phrases like "Crafting remarkable living rooms" this belongs tpo one of our suppliers so can not be used.
Nice to have
• Double sided, so front dedicated to logo provided and back info about the business and the person.

```html
<!DOCTYPE html>
<html lang="en">
<head>
<meta charset="utf-8">
<title>Meridian Interiors — Business Card</title>
<link rel="stylesheet" href="https://fonts.googleapis.com/css2?family=Montserrat:wght@400;600&display=swap">
<style>
  :root{
    --page:#fcfafb;
    --card:#ffffff;
    --charcoal:#333333;
    --slate:#5c5c5c;
    --ink:#111111;
    --light:#ffffff;
  }
  *{box-sizing:border-box;margin:0;padding:0}
  html,body{width:1200px;height:1200px;overflow:hidden}
  body{background:var(--page);font-family:"Montserrat",Arial,sans-serif;position:relative}

  .card{position:absolute;background:var(--card)}
  .card--front{left:259px;top:123px;width:700px;height:416px}
  .card--back{left:260px;top:624px;width:701px;height:420px}

  .front-panel{position:absolute;left:22px;top:23px;width:655px;height:316px;background:var(--charcoal)}
  .front-stripe{position:absolute;left:22px;top:339px;width:655px;height:34px;background:var(--card);border-left:1px solid #e6e6e6;border-right:1px solid #e6e6e6}
  .front-base{position:absolute;left:22px;top:373px;width:655px;height:22px;background:var(--charcoal)}

  .brand{position:absolute;display:flex;align-items:center;gap:14px;font-weight:400}
  .brand__mark{border-radius:50%;flex:none}
  .brand__name{display:flex;flex-direction:column;align-items:center;line-height:1}
  .brand__word{letter-spacing:.42em;text-transform:uppercase}
  .brand__sub{letter-spacing:.42em;text-transform:uppercase;margin-top:.9em}

  .brand--front{left:162px;top:170px;color:var(--light)}
  .brand--front .brand__mark{width:46px;height:46px;border:2px solid var(--light)}
  .brand--front .brand__word{font-size:26px}
  .brand--front .brand__sub{font-size:11px}

  .brand--back{left:50%;transform:translateX(-50%);top:318px;color:var(--ink)}
  .brand--back .brand__mark{width:30px;height:30px;border:2px solid var(--ink)}
  .brand--back .brand__word{font-size:15px}
  .brand--back .brand__sub{font-size:6.5px}

  .info-band{position:absolute;left:22px;top:126px;width:657px;height:168px;background:var(--slate);color:var(--light)}
  .person{position:absolute;left:82px;top:22px}
  .person__name{font-size:17px;font-weight:600;letter-spacing:.01em}
  .person__role{font-size:15px;font-weight:400;margin-top:3px}

  .contact{position:absolute;left:80px;display:flex;align-items:center;gap:18px;font-size:13px;letter-spacing:.02em}
  .contact--phone{top:82px}
  .contact--mail{top:110px}
  .contact__icon{width:22px;height:22px;flex:none}

  .divider{position:absolute;left:328px;top:42px;width:2px;height:85px;background:var(--light)}
  .address{position:absolute;left:377px;top:66px;font-size:13px;line-height:19px;letter-spacing:.02em}
</style>
</head>
<body>

<section class="card card--front" aria-label="Card front">
  <div class="front-panel">
    <div class="brand brand--front">
      <span class="brand__mark"></span>
      <span class="brand__name">
        <span class="brand__word">Meridian</span>
        <span class="brand__sub">Interiors</span>
      </span>
    </div>
  </div>
  <div class="front-stripe"></div>
  <div class="front-base"></div>
</section>

<section class="card card--back" aria-label="Card back">
  <div class="info-band">
    <div class="person">
      <p class="person__name">NEIL DAWSON</p>
      <p class="person__role">Director</p>
    </div>

    <div class="contact contact--phone">
      <svg class="contact__icon" viewBox="0 0 22 22" aria-hidden="true">
        <circle cx="11" cy="11" r="11" fill="#fff"/>
        <path d="M7.2 5.6c.5-.4 1.2-.3 1.5.2l1.1 1.8c.3.5.2 1.1-.2 1.4l-.7.6c.5 1.3 1.6 2.6 3 3.3l.6-.7c.4-.4 1-.5 1.4-.2l1.8 1.1c.5.3.6 1 .2 1.5l-.8.9c-.6.6-1.5.8-2.3.5-3-1.1-5.3-3.5-6.3-6.5-.3-.8 0-1.7.6-2.3z" fill="#5c5c5c"/>
      </svg>
      <span>+64219473815</span>
    </div>

    <div class="contact contact--mail">
      <svg class="contact__icon" viewBox="0 0 22 22" aria-hidden="true">
        <circle cx="11" cy="11" r="11" fill="#fff"/>
        <rect x="5.5" y="7.5" width="11" height="7.5" rx="1" fill="#5c5c5c"/>
        <path d="M5.8 8l5.2 4 5.2-4M5.8 14.6l3.6-3.2M16.2 14.6l-3.6-3.2" stroke="#fff" stroke-width=".9" fill="none"/>
      </svg>
      <span>www.youremail@.com</span>
    </div>

    <div class="divider"></div>

    <p class="address">Your Location Address<br>Here</p>
  </div>

  <div class="brand brand--back">
    <span class="brand__mark"></span>
    <span class="brand__name">
      <span class="brand__word">Meridian</span>
      <span class="brand__sub">Interiors</span>
    </span>
  </div>
</section>

</body>
</html>
```